3 -4 PAGE GIFT CERTIFICATE REDEMPTION WEBSITE REVAMP

I am revamping the entire website at www.brightperksportal.net

Will have brand new theme and new logo. Name Of Company:
Bounty Motivation Delivery Networks
BMDN

OVERVIEW:
I NEED A 3-4 PAGE WEBSITE DESIGNED WITH CHECKOUT MODULE.
My company offers fully brandable and personalizable gift certificates good for travel, vacations, dining rewards, rebates, electronic gifts, etc. and I need to redesign the website where the fulfillment and redemption happens.

So the way it works is a business uses my online platform to create, brand and personalize these gift certificates. The business can brand the certificates in the upper right hand corner of each certificate where the “Compliments Of” area sits with their company logo, website, contact info, etc and can also personalize each individual gift certificate to a specific customer too. SEE EXAMPLE ATTACHED TO BRIEF.

The example I attached to this brief includes a logo which is really just a picture and under it there is 3 lines of text where the business can put a website, phone number and email.

On the left side of the top banner image you will see “Exclusively For”.

So now, after a customer enters their certificate ID #, the branding on the next page must match the Compliments Of area and also must personalize the Sales Page to the customer that is in the Exclusively For” area of the certificate…...

Page 1: LANDING PAGE
CONTENT:

Welcome to the online redemption source for vacation certificates, travel vouchers, digital electronic products, dining incentives, gas and grocery rewards and more!

ENTER YOUR CERTIFICATE ID #
ENTER YOUR EMAIL

Welcome to the online redemption system for vacation certificates, travel vouchers, rebates, digital products, dining incentives, gas and grocery rewards and more!

PLEASE ENTER A VALID CERTIFICATE ID NUMBER TO VIEW THE DETAILS AND TO REDEEM AND ACTIVATE YOUR SPECIAL OFFER.

Also we need a testimonial module ON THIS PAGE AND SALES PAGE

PAGE 2: SALES PAGE FOR OFFER (we will use the 1-4 Night Las Vegas Hotel Stay Certificate)
INSTRUCTIONS EXPLANATION FOR DESIGNER: Every gift certificate has a "Compliments Of Area" in the upper right hand corner....SEE SAMPLE ATTACHED TO BRIEF. On the sales page we also show this to the customer after they enter the code. Every certificate has a Compliments Of area and we will also add "Exclusively For" so the person that is giving the certificate away can specify the name of the recipient so we will also transffer this information over to the SALES PAGE.

CONTENT FOR SALES PAGE:

WELCOME ~~NAME OF PERSON IN EXCLUSIVELY FOR AREA ON CERTIFICATE~~ !!

THIS SPECIAL INCENTIVE OFFER IS COMPLIMENTS OF

~~LOGO THAT IS SEEN ON CERTIFICATE~~
~~TEXT LINE 1~~
~~TEXT LINE 2~~
~~TEXT LINE 3~~

TITLE OF OFFER: STAY & PLAY IN LAS VEGAS FOR UP TO 4 NIGHTS!
There is no doubt that Las Vegas is one of the hottest travel destinations around the world. In fact, some people would even go as far as saying that perhaps it is THE hottest place to visit. Enjoy up to 4 nights of resort/casino accommodations in exciting Las Vegas, NV. Millions of people travel to this exciting city each year to enjoy its thrills. Thanks to the business you received this certificate from, now you can enjoy Las Vegas, NV too!

Features:
*Travel 7 Days A Week
*Stay Your Choice Of Nights (1-4 Nights)
*Good For Two Adults & Two Children
*Pay Just The Taxes & Fees
*Multiple Travel Date Requests Allowed
*Fully Transferable To Another Person
*Just A 30 Days Advance Notice Required
*You Will Have 12 Months To Complete Travel

HOW CAN WE DO THIS?

We contract with the world leading hotel chains and resorts to help them fill their otherwise empty rooms.

We help fill empty rooms which the hotels, resorts and cruise lines turn into additional revenue from other areas of their property and future bookings.

Hotels rarely experience full occupancy, yet they remain open, providing rooms and services at fixed costs. So when hotels give out their rooms by partnering with marketing companies like us, they might miss out on the room fee, but they already didn't have that in the first place, at least now they have the opportunity to gain a customer for their in-house restaurants, room service, their casinos, an extra day stay, future bookings, etc.

The magic of why our program works so well is the fact that it’s a win win for everyone involved. You win because you received a huge savings. The business who gave you the certificate wins because now you will remember them the next time you need the same kind of product or service that they provide and you might even refer your friends and family members. The hotels and resorts win because they gain additional revenue from other areas of their establishment that they otherwise would not have been able to get and they also have a new client that may book with them in the future. Remember, they didn’t have anyone in the room in the first place so since you are paying the normal rack rate you might be more inclined to spend your money at the hotel. You are never under any obligation to do so though!

Retail Value: Up to $826.00 (based on $159.00 per night)

How it Works:
You will receive up to 4 nights in a 3 star or better Las Vegas resort and casino for up to 4 travelers, 2 adults and 2 children.

Simply redeem the certificate to activate the travel period for 1 year. This means you will have at least 1 year to travel from the date you redeem and activate your offer. Be sure to redeem your certificate before it expires! All certificates will have an accompanying expiration date attached to them.

When you are ready to book you will simply have to pay the daily room rate taxes and fees of approximately $12-$33 per night (not per person). On average the taxes and fees come out to about $19 per night. (Retail Value: Up to $826.00 based on $159.00 per night)

Step 1: Redeem your certificate to activate your offer

Step 2: Fill out the online reservation request form with travel dates within the next 12 months.

Step 3: Wait for a confirmation of your booked reservation. You will be notified immediately upon us booking your reservation.

Go on your vacation and thank the business who gave you this special offer by doing business with them again and referring your friends and family members!

No timeshares or sales presentations, Guaranteed!

PAGE 3 IS CHECKOUT PAGE:

PLEASE USE ****HERE IS SAMPLE CODE FOR YOU TO TEST OUT AT CURRENT REDEMPTION PROCESS WWW.BRIGHTPERKSPORTAL.NET 46205-17938

TO SEE THE CURRENT CHECK OUT. I NEED ALL THE SAME CONTENT JUST A DIFFERENT MORE EFFICIENT CHECKOUT PROCESS HERE. OMIT THE LEFT SIDE OF THE CURRENT CHECK OUT PROCESS AS THIS CURRENT PROCESSS IS ONE STEP AND DOES NOT HAVE A SALES PAGE BUT NOW I AM CREATING A SALES PAGE BEFORE THE CHECKOUT SO THE BRANDING AND PERSONALIZATION WILL HAPPEN ON THE SALES PAGE….THANK YOU

Target Market(s)

END USERS THAT ARE REDEEMING SPECIAL OFFERS GIFT CERTIFICATES

Industry/Entity Type

Marketing

Number of Pages Required

4 page

Colors

Designer to choose colors to be used in the design.

Requirements
Must have
• OVERVIEW:
• I NEED A 3-4 PAGE WEBSITE DESIGNED WITH CHECKOUT MODULE.
• My company offers fully brandable and personalizable gift certificates good for travel, vacations, dining rewards, rebates, electronic gifts, etc. and I need to redesign the website where the fulfillment and redemption happens.
• So the way it works is a business uses my online platform to create, brand and personalize these gift certificates. The business can brand the certificates in the upper right hand corner of each certificate where the “Compliments Of” area sits with their company logo, website, contact info, etc and can also personalize each individual gift certificate to a specific customer too. SEE EXAMPLE ATTACHED TO BRIEF.
• The example I attached to this brief includes a logo which is really just a picture and under it there is 3 lines of text where the business can put a website, phone number and email.
• On the left side of the top banner image you will see “Exclusively For”.
• So now, after a customer enters their certificate ID #, the branding on the next page must match the Compliments Of area and also must personalize the Sales Page to the customer that is in the Exclusively For” area of the certificate…...
• Page 1: LANDING PAGE
• CONTENT:
• Welcome to the online redemption source for vacation certificates, travel vouchers, digital electronic products, dining incentives, gas and grocery rewards and more!
• ENTER YOUR CERTIFICATE ID #
• ENTER YOUR EMAIL
• Welcome to the online redemption system for vacation certificates, travel vouchers, rebates, digital products, dining incentives, gas and grocery rewards and more!
• PLEASE ENTER A VALID CERTIFICATE ID NUMBER TO VIEW THE DETAILS AND TO REDEEM AND ACTIVATE YOUR SPECIAL OFFER.
• Also we need a testimonial module ON THIS PAGE AND SALES PAGE
• PAGE 2: SALES PAGE FOR OFFER (we will use the 1-4 Night Las Vegas Hotel Stay Certificate)
• INSTRUCTIONS EXPLANATION FOR DESIGNER: Every gift certificate has a "Compliments Of Area" in the upper right hand corner....SEE SAMPLE ATTACHED TO BRIEF. On the sales page we also show this to the customer after they enter the code. Every certificate has a Compliments Of area and we will also add "Exclusively For" so the person that is giving the certificate away can specify the name of the recipient so we will also transffer this information over to the SALES PAGE.
• CONTENT FOR SALES PAGE:
• WELCOME ~~NAME OF PERSON IN EXCLUSIVELY FOR AREA ON CERTIFICATE~~ !!
• THIS SPECIAL INCENTIVE OFFER IS COMPLIMENTS OF
• ~~LOGO THAT IS SEEN ON CERTIFICATE~~
• ~~TEXT LINE 1~~
• ~~TEXT LINE 2~~
• ~~TEXT LINE 3~~
• TITLE OF OFFER: STAY & PLAY IN LAS VEGAS FOR UP TO 4 NIGHTS!
• There is no doubt that Las Vegas is one of the hottest travel destinations around the world. In fact, some people would even go as far as saying that perhaps it is THE hottest place to visit. Enjoy up to 4 nights of resort/casino accommodations in exciting Las Vegas, NV. Millions of people travel to this exciting city each year to enjoy its thrills. Thanks to the business you received this certificate from, now you can enjoy Las Vegas, NV too!
• Features:
• *Travel 7 Days A Week
• *Stay Your Choice Of Nights (1-4 Nights)
• *Good For Two Adults & Two Children
• *Pay Just The Taxes & Fees
• *Multiple Travel Date Requests Allowed
• *Fully Transferable To Another Person
• *Just A 30 Days Advance Notice Required
• *You Will Have 12 Months To Complete Travel
• HOW CAN WE DO THIS?
• We contract with the world leading hotel chains and resorts to help them fill their otherwise empty rooms.
• We help fill empty rooms which the hotels, resorts and cruise lines turn into additional revenue from other areas of their property and future bookings.
• Hotels rarely experience full occupancy, yet they remain open, providing rooms and services at fixed costs. So when hotels give out their rooms by partnering with marketing companies like us, they might miss out on the room fee, but they already didn't have that in the first place, at least now they have the opportunity to gain a customer for their in-house restaurants, room service, their casinos, an extra day stay, future bookings, etc.
• The magic of why our program works so well is the fact that it’s a win win for everyone involved. You win because you received a huge savings. The business who gave you the certificate wins because now you will remember them the next time you need the same kind of product or service that they provide and you might even refer your friends and family members. The hotels and resorts win because they gain additional revenue from other areas of their establishment that they otherwise would not have been able to get and they also have a new client that may book with them in the future. Remember, they didn’t have anyone in the room in the first place so since you are paying the normal rack rate you might be more inclined to spend your money at the hotel. You are never under any obligation to do so though!
• Retail Value: Up to $826.00 (based on $159.00 per night)
• How it Works:
• You will receive up to 4 nights in a 3 star or better Las Vegas resort and casino for up to 4 travelers, 2 adults and 2 children.
• Simply redeem the certificate to activate the travel period for 1 year. This means you will have at least 1 year to travel from the date you redeem and activate your offer. Be sure to redeem your certificate before it expires! All certificates will have an accompanying expiration date attached to them.
• When you are ready to book you will simply have to pay the daily room rate taxes and fees of approximately $12-$33 per night (not per person). On average the taxes and fees come out to about $19 per night. (Retail Value: Up to $826.00 based on $159.00 per night)
• Step 1: Redeem your certificate to activate your offer
• Step 2: Fill out the online reservation request form with travel dates within the next 12 months.
• Step 3: Wait for a confirmation of your booked reservation. You will be notified immediately upon us booking your reservation.
• Go on your vacation and thank the business who gave you this special offer by doing business with them again and referring your friends and family members!
• No timeshares or sales presentations, Guaranteed!
• PAGE 3 IS CHECKOUT PAGE:
• PLEASE USE ****HERE IS SAMPLE CODE FOR YOU TO TEST OUT AT CURRENT REDEMPTION PROCESS WWW.BRIGHTPERKSPORTAL.NET 46205-17938
• TO SEE THE CURRENT CHECK OUT. I NEED ALL THE SAME CONTENT JUST A DIFFERENT MORE EFFICIENT CHECKOUT PROCESS HERE. OMIT THE LEFT SIDE OF THE CURRENT CHECK OUT PROCESS AS THIS CURRENT PROCESSS IS ONE STEP AND DOES NOT HAVE A SALES PAGE BUT NOW I AM CREATING A SALES PAGE BEFORE THE CHECKOUT SO THE BRANDING AND PERSONALIZATION WILL HAPPEN ON THE SALES PAGE….THANK YOU
Nice to have
• OVERVIEW:
• Page 1: LANDING PAGE
• CONTENT:
• ENTER YOUR EMAIL
• CONTENT FOR SALES PAGE:
• ~~TEXT LINE 1~~
• ~~TEXT LINE 2~~
• ~~TEXT LINE 3~~
• Features:
• *Travel 7 Days A Week
• HOW CAN WE DO THIS?
• How it Works:
Should not have
• OVERVIEW:
• Page 1: LANDING PAGE
• CONTENT:
• ENTER YOUR EMAIL
• CONTENT FOR SALES PAGE:
• ~~TEXT LINE 1~~
• ~~TEXT LINE 2~~
• ~~TEXT LINE 3~~
• Features:
• *Travel 7 Days A Week
• HOW CAN WE DO THIS?
• How it Works:

```html
<!DOCTYPE html>
<html lang="en">
<head>
<meta charset="utf-8">
<title>Bounty Motivation Delivery Networks – Las Vegas Offer</title>
<link href="https://fonts.googleapis.com/css2?family=Jost:wght@400;500;600;700&family=Roboto+Condensed:wght@400;500;700&display=swap" rel="stylesheet">
<style>
:root{
  --yellow:#fbbd23;
  --yellow-light:#fdd064;
  --orange:#f37021;
  --orange-dark:#d95a12;
  --navy:#0f2d4f;
  --navy-deep:#0c2744;
  --maroon:#2e0205;
  --ink:#2a2a2a;
  --grey-bg:#efefef;
  --white:#ffffff;
}
*{box-sizing:border-box;margin:0;padding:0}
html,body{width:1200px;height:5398px;overflow:hidden}
body{font-family:"Jost",sans-serif;color:var(--ink);background:var(--white);position:relative}
section,footer,header{position:absolute;left:0;width:1200px}
.abs{position:absolute}
.btn{position:absolute;display:flex;align-items:center;justify-content:center;background:var(--orange);color:var(--white);font-family:"Roboto Condensed",sans-serif;font-weight:700;font-size:14px;letter-spacing:.2px;border-radius:4px;box-shadow:0 3px 0 var(--orange-dark);text-transform:uppercase}
.section-title{position:absolute;font-family:"Roboto Condensed",sans-serif;font-weight:500;font-size:32px;color:var(--ink);text-transform:uppercase;text-align:center}
.section-title.underlined::after{content:"";display:block;height:2px;background:currentColor;margin-top:6px;opacity:.7}

/* hero */
.hero{top:0;height:1040px;background:var(--yellow);overflow:hidden}
.brand-name{position:absolute;left:157px;top:12px;font-family:"Jost",sans-serif;font-weight:700;font-size:22px;line-height:24px;color:var(--navy);width:300px}
.hero-photo{position:absolute;left:0;top:70px;width:1120px;height:440px;border-radius:0 160px 0 220px;background:linear-gradient(180deg,#b9d2e6 0%,#dfe3df 35%,#d8b98a 70%,#c79a5e 100%)}
.cert-box{position:absolute;left:785px;top:0;width:255px;height:262px;background:var(--white);text-align:center;box-shadow:0 2px 8px rgba(0,0,0,.15)}
.cert-box .cert-head{color:var(--orange);font-weight:600;font-size:15px;line-height:17px;margin-top:8px;text-transform:uppercase}
.cert-logo{width:210px;height:82px;margin:6px auto 0;background:linear-gradient(180deg,#9fc3e0,#d7c6a0)}
.cert-box .courtesy{color:var(--navy);font-size:13px;margin-top:8px;font-weight:500}
.cert-box .line{font-size:12.5px;color:var(--ink);margin-top:3px;display:flex;align-items:center;justify-content:center;gap:5px}
.exclusive-bar{position:absolute;left:255px;top:460px;width:740px;height:55px;background:var(--orange);color:var(--white);font-size:22px;font-weight:500;padding-left:80px;display:flex;align-items:center;text-transform:uppercase}
.title-banner{position:absolute;left:255px;top:517px;width:790px;height:105px}
.title-banner span{position:absolute;left:0;top:0;width:740px;height:105px;display:flex;align-items:center;justify-content:center;color:var(--white);font-weight:600;font-size:37px;letter-spacing:.5px}
.skyline{position:absolute;left:0;top:840px;width:1200px;height:200px;background:linear-gradient(180deg,rgba(253,208,100,0) 0%,rgba(230,160,40,.35) 100%)}
.offer-label{left:0;width:1200px;top:668px}
.offer-title{position:absolute;left:0;width:1200px;top:728px;text-align:center;font-weight:700;font-size:31px;color:var(--ink);text-transform:uppercase}
.offer-copy{position:absolute;left:240px;width:720px;top:772px;text-align:center;font-size:13.5px;line-height:19px;color:var(--ink)}

/* features */
.features{top:1040px;height:530px}
.photo{position:absolute;box-shadow:0 3px 8px rgba(0,0,0,.2)}
.features .photo{left:157px;top:88px;width:450px;height:359px;background:linear-gradient(180deg,#7fb3dd 0%,#2d7fb8 45%,#3a9a8a 70%,#d8d4c0 100%)}
.side-title{position:absolute;font-family:"Roboto Condensed",sans-serif;font-weight:500;font-size:32px;color:var(--ink);text-transform:uppercase}
.features .side-title{left:680px;top:80px}
.dot-list{position:absolute;list-style:none}
.dot-list li{position:relative;padding-left:25px;font-size:14px;line-height:28.7px;color:var(--ink)}
.dot-list li::before{content:"";position:absolute;left:2px;top:12px;width:6px;height:6px;border-radius:50%;background:var(--ink)}
.features .dot-list{left:680px;top:137px}

/* how can we */
.how-can{top:1570px;height:629px;background:var(--maroon);color:var(--white)}
.how-can .section-title{color:var(--white);left:440px;width:320px;top:78px}
.col-text{position:absolute;list-style:none;font-size:12.5px;line-height:18.8px}
.col-text li{position:relative;padding-left:25px;margin-bottom:19px}
.col-text li::before{content:"";position:absolute;left:2px;top:6px;width:6px;height:6px;border-radius:50%;background:var(--white)}
.col-left{left:157px;top:160px;width:430px}
.col-right{left:618px;top:160px;width:430px}
.col-divider{position:absolute;left:600px;top:158px;width:1px;height:310px;background:rgba(255,255,255,.2)}
.value-banner{position:absolute;left:205px;top:2146px;width:795px;height:105px;z-index:3}
.value-banner .txt{position:absolute;left:0;top:0;width:740px;height:105px;display:flex;flex-direction:column;align-items:center;justify-content:center;color:var(--white)}
.value-banner .big{font-size:32px;font-weight:600;line-height:36px}
.value-banner .small{font-size:22px;font-weight:500;line-height:26px}

/* how it works */
.how-works{top:2199px;height:691px}
.how-works .photo{left:157px;top:138px;width:436px;height:465px;background:linear-gradient(180deg,#1e2b4a 0%,#5d6e8a 40%,#c8a36b 62%,#2d5d88 100%)}
.how-works .side-title{left:680px;top:128px}
.how-works .dot-list{left:680px;top:195px;width:370px}
.how-works .dot-list li{font-size:13px;line-height:19px;margin-bottom:17px}
.how-works .dot-list li::before{top:7px}

/* testimonials */
.testimonials{top:2890px;height:670px;background:var(--grey-bg)}
.testimonials .section-title{left:450px;width:300px;top:48px}
.t-card{position:absolute;background:var(--white);padding:22px 22px;font-size:13px;line-height:19px;color:var(--ink);display:flex;align-items:center}
.t-card::after{content:"";position:absolute;left:30px;bottom:-18px;border-left:0 solid transparent;border-right:22px solid transparent;border-top:18px solid var(--white)}
.t-author{position:absolute;display:flex;gap:14px;font-size:12px;line-height:15px}
.avatar{width:52px;height:52px;flex:none}
.t-author .name{color:var(--navy);font-weight:600;text-transform:uppercase}
.t-author .place{font-weight:500;color:var(--ink)}
.dots{position:absolute;left:582px;top:536px;display:flex;gap:6px}
.dots i{width:7px;height:7px;border-radius:50%;border:1px solid #888;display:block}
.dots i.on{background:#444;border-color:#444}

/* video */
.video{top:3560px;height:702px}
.video .section-title{left:430px;width:340px;top:94px}
.video-frame{position:absolute;left:161px;top:153px;width:878px;height:396px;background:linear-gradient(180deg,#c9d6e3 0%,#e9c9cf 30%,#5fc6e6 55%,#8ad9ef 100%);box-shadow:0 3px 8px rgba(0,0,0,.25);border:4px solid var(--white)}
.play{position:absolute;left:389px;top:150px;width:92px;height:92px;border-radius:50%;background:rgba(255,255,255,.55);display:flex;align-items:center;justify-content:center}

/* steps */
.steps{top:4262px;height:398px;background:linear-gradient(135deg,var(--yellow) 0%,var(--yellow-light) 55%,var(--yellow) 100%)}
.step{position:absolute;width:230px;text-align:center}
.step .num{font-weight:600;font-size:80px;line-height:80px;color:var(--maroon)}
.step p{font-size:13.5px;line-height:20px;margin-top:20px;color:var(--ink)}

/* closing */
.closing{top:4660px;height:355px;text-align:center}
.closing .lead{position:absolute;left:170px;width:860px;top:80px;font-size:19px;line-height:27px;color:var(--ink)}
.closing .claim{position:absolute;left:0;width:1200px;top:146px;font-weight:600;font-size:29px;line-height:38px;color:var(--maroon);letter-spacing:1px}
.closing .claim b{display:block;font-size:35px;letter-spacing:2px}

/* footer */
.site-footer{top:5015px;height:383px;background:var(--navy-deep);color:var(--white)}
.f-col{position:absolute;top:100px;width:290px}
.f-col h3{font-size:16px;font-weight:500;text-transform:uppercase;margin-bottom:22px}
.f-col p{font-size:12.5px;line-height:18px;color:#d9e1ea}
.f-contact{display:flex;gap:12px}
.f-rule{position:absolute;left:157px;top:277px;width:886px;height:1px;background:rgba(255,255,255,.2)}
.copyright{position:absolute;left:0;width:1200px;top:318px;text-align:center;font-size:11.5px;color:#d9e1ea}
</style>
</head>
<body>

<header class="hero">
  <div class="hero-photo" role="img" aria-label="Panoramic photo of the Las Vegas Strip with resort towers and fountains"></div>
  <div class="skyline" role="img" aria-label="Line illustration of a city skyline with towers and monuments"></div>
  <div class="brand-name">Bounty Motivation<br>Delivery Networks</div>

  <div class="cert-box">
    <div class="cert-head">This certificate is<br>compliments of</div>
    <div class="cert-logo" role="img" aria-label="Sponsoring business image"></div>
    <div class="courtesy">Certificate Courtesy Of</div>
    <div class="line"><svg width="11" height="9" viewBox="0 0 11 9"><rect x=".5" y=".5" width="10" height="8" fill="none" stroke="#2a2a2a"/><path d="M.5 .5 5.5 5 10.5 .5" fill="none" stroke="#2a2a2a"/></svg>hello@bountyperksmail.net</div>
    <div class="line"><svg width="9" height="11" viewBox="0 0 9 11"><path d="M2 1h2l1 3-1.5 1a6 6 0 0 0 2 3L7 7l2 1v2c-4 0-8-4-8-8z" fill="#2a2a2a"/></svg>555-204-318</div>
    <div class="line"><svg width="11" height="11" viewBox="0 0 11 11"><circle cx="5.5" cy="5.5" r="5" fill="none" stroke="#2a2a2a"/><path d="M.5 5.5h10M5.5 .5c-3 3-3 7 0 10M5.5 .5c3 3 3 7 0 10" fill="none" stroke="#2a2a2a"/></svg>http://bountyperksmail.net</div>
  </div>

  <div class="exclusive-bar">Exclusive for : Lorem Ipsum</div>
  <div class="title-banner">
    <svg class="abs" width="790" height="105" viewBox="0 0 790 105"><polygon points="0,0 740,0 790,52 740,105 0,105" fill="#0f2d4f"/></svg>
    <span>UP TO 4 NIGHTS IN LAS VEGAS!</span>
  </div>

  <h2 class="section-title underlined offer-label" style="width:160px;left:520px">Our Offer</h2>
  <h1 class="offer-title">Stay &amp; Play in Las Vegas for up to 4 Nights!</h1>
  <p class="offer-copy">There is no doubt that Las Vegas is one of the hottest travel destinations around the world. In fact, some people would even go as far as saying that perhaps it is THE hottest place to visit. Enjoy up to 4 nights of resort/casino accommodations in exciting Las Vegas, NV. Millions of people travel to this exciting city each year to enjoy its thrills. Thanks to the business you received this certificate from, now you can enjoy Las Vegas, NV too!</p>
  <a class="btn" style="left:463px;top:890px;width:274px;height:48px">Redeem &amp; Activate Your Offer Now</a>
</header>

<section class="features">
  <div class="photo" role="img" aria-label="Resort infinity pool overlooking the ocean with palm trees"></div>
  <h2 class="side-title">Features:</h2>
  <ul class="dot-list">
    <li>Travel 7 Days A Week</li>
    <li>Stay Your Choice Of Nights (1-4 Nights)</li>
    <li>Good For Two Adults &amp; Two Children</li>
    <li>Pay Just The Taxes &amp; Fees</li>
    <li>Multiple Travel Date Requests Allowed</li>
    <li>Fully Transferable To Another Person</li>
    <li>Just A 30 Days Advance Notice Required</li>
    <li>You Will Have 12 Months To Complete Travel</li>
  </ul>
  <a class="btn" style="left:680px;top:390px;width:277px;height:47px">Redeem &amp; Activate Your Offer Now</a>
</section>

<section class="how-can">
  <h2 class="section-title underlined">How Can We Do This?</h2>
  <ul class="col-text col-left">
    <li>We contract with the world leading hotel chains and resorts to help them fill their otherwise empty rooms.</li>
    <li>We help fill empty rooms which the hotels, resorts and cruise lines turn into additional revenue from other areas of their property and future bookings.</li>
    <li>Hotels rarely experience full occupancy, yet they remain open, providing rooms and services at fixed costs. So when hotels give out their rooms by partnering with marketing companies like us, they might miss out on the room fee, but they already didn't have that in the first place, at least now they have the opportunity to gain a customer for their in-house restaurants, room service, their casinos, an extra day stay, future bookings, etc.</li>
  </ul>
  <div class="col-divider"></div>
  <ul class="col-text col-right">
    <li>The magic of why our program works so well is the fact that it’s a win win for everyone involved. You win because you received a huge savings. The business who gave you the certificate wins because now you will remember them the next time you need the same kind of product or service that they provide and you might even refer your friends and family members. The hotels and resorts win because they gain additional revenue from other areas of their establishment that they otherwise would not have been able to get and they also have a new client that may book with them in the future. Remember, they didn’t have anyone in the room in the first place so since you are paying the normal rack rate you might be more inclined to spend your money at the hotel. You are never under any obligation to do so though!</li>
  </ul>
  <a class="btn" style="left:462px;top:472px;width:276px;height:48px">Redeem &amp; Activate Your Offer Now</a>
</section>

<div class="value-banner">
  <svg class="abs" width="795" height="105" viewBox="0 0 795 105"><polygon points="0,0 795,0 740,105 0,105" fill="#0f2d4f"/></svg>
  <div class="txt"><span class="big">RETAIL VALUE: UP TO $826.00</span><span class="small">(BASED ON $159.00 PER NIGHT)</span></div>
</div>

<section class="how-works">
  <div class="photo" role="img" aria-label="Modern resort villa at dusk reflected in a still pool"></div>
  <h2 class="side-title">How It Works</h2>
  <ul class="dot-list">
    <li>You will receive up to 4 nights in a 3 star or better Las Vegas resort and casino for up to 4 travelers, 2 adults and 2 children.</li>
    <li>Simply redeem the certificate to activate the travel period for 1 year. This means you will have at least 1 year to travel from the date you redeem and activate your offer. Be sure to redeem your certificate before it expires! All certificates will have an accompanying expiration date attached to them.</li>
    <li>When you are ready to book you will simply have to pay the daily room rate taxes and fees of approximately $12-$33 per night (not per person). On average the taxes and fees come out to about $19 per night. (Retail Value: Up to $826.00 based on $159.00 per night)</li>
  </ul>
  <a class="btn" style="left:684px;top:555px;width:276px;height:48px">Redeem &amp; Activate Your Offer Now</a>
</section>

<section class="testimonials">
  <h2 class="section-title underlined">Client Testimonial</h2>
  <div class="t-card" style="left:157px;top:145px;width:283px;height:228px">"It was really a good time! It was so great, and everything was well organized by our travel agency. No surprise or disappointment . Thank you guys, we will contact you again!"</div>
  <div class="t-card" style="left:457px;top:198px;width:284px;height:175px">"Very good. Las Vegas was a dream trip. Would go again without a doubt. It's the best. The hotels, the streets, the Grand Canyon. Everything is very good! "</div>
  <div class="t-card" style="left:756px;top:145px;width:284px;height:228px;align-items:flex-start">Wonderful! It was just like being in Rome, but only with great shows to enjoy. The rooms of the Solara and service were excellent. Going through the travel agency was simple and easy on the purse strings."</div>

  <div class="t-author" style="left:157px;top:418px"><div class="avatar" role="img" aria-label="Client photo" style="background:linear-gradient(#8aa3c0,#5a6b80)"></div><div><div class="name">Marcus T.</div><div class="place">Miami Gardens, FL</div><div>Added on 12/04/2019 07:18:14 pm</div></div></div>
  <div class="t-author" style="left:457px;top:418px"><div class="avatar" role="img" aria-label="Client photo" style="background:linear-gradient(#3a3550,#a0506a)"></div><div><div class="name">Lena P.</div><div class="place">Orlando, FL</div><div>Added on 12/04/2019 06:49:47 pm</div></div></div>
  <div class="t-author" style="left:756px;top:418px"><div class="avatar" role="img" aria-label="Client photo" style="background:linear-gradient(#c79b6a,#8a5a3a)"></div><div><div class="name">Owen K.</div><div class="place">Flagstaff, AZ</div><div>Added on 01/21/2020 09:03:06 pm</div></div></div>

  <div class="dots"><i></i><i class="on"></i><i></i></div>
  <a class="btn" style="left:462px;top:565px;width:276px;height:49px">Redeem &amp; Activate Your Offer Now</a>
</section>

<section class="video">
  <h2 class="section-title underlined">Enjoy Viva Las Vegas</h2>
  <div class="video-frame" role="img" aria-label="Video still of a rooftop resort pool with loungers and palm trees">
    <div class="play"><svg width="30" height="32" viewBox="0 0 30 32"><polygon points="4,2 28,16 4,30" fill="#e21c1c"/></svg></div>
  </div>
  <a class="btn" style="left:462px;top:582px;width:276px;height:48px">Redeem &amp; Activate Your Offer Now</a>
</section>

<section class="steps">
  <svg class="abs" style="left:0;top:0" width="1200" height="398" viewBox="0 0 1200 398">
    <g fill="none" stroke="#7a4a10" stroke-width="1.4" stroke-dasharray="3 5" opacity=".6">
      <path d="M160 228 C150 140 250 80 330 95 C420 110 440 150 470 130 C520 80 640 60 700 110"/>
      <path d="M720 118 C760 60 860 60 920 100 C1010 160 1060 200 1030 320"/>
      <path d="M470 170 C480 260 520 300 620 300 C700 300 720 260 760 200"/>
    </g>
    <circle cx="158" cy="230" r="3.5" fill="#2e0205"/>
    <circle cx="1032" cy="324" r="3.5" fill="#2e0205"/>
  </svg>
  <div class="step" style="left:185px;top:118px"><div class="num">1.</div><p>Redeem your certificate to activate your offer</p></div>
  <div class="step" style="left:485px;top:118px"><div class="num">2.</div><p>Fill out the online reservation request form with travel dates within the next 12 months.</p></div>
  <div class="step" style="left:790px;top:118px"><div class="num">3.</div><p>Wait for a confirmation of your booked reservation. You will be notified immediately upon us booking your reservation.</p></div>
</section>

<section class="closing">
  <p class="lead">Go on your vacation and thank the business who gave you this special offer by doing business with them again and referring your friends and family members!</p>
  <div class="claim">NO TIMESHARES OR SALES PRESENTATIONS,<b>GUARANTEED!</b></div>
  <a class="btn" style="left:462px;top:240px;width:276px;height:53px">Redeem &amp; Activate Your Offer Now</a>
</section>

<footer class="site-footer">
  <div class="f-col" style="left:157px"><h3>Have Questions?</h3><p>We are here to help you redeem your certificates Feel free to contact us with any questions or suggestions on how we can do our job better.</p></div>
  <div class="f-col" style="left:496px;width:250px"><h3>Terms &amp; Conditions</h3><p>long established fact that a reader will be distracted by the readable content of a page when looking at its layout.</p></div>
  <div class="f-col" style="left:823px"><h3>Contact Us</h3>
    <div class="f-contact"><svg width="14" height="18" viewBox="0 0 14 18"><path d="M7 0a7 7 0 0 0-7 7c0 5 7 11 7 11s7-6 7-11a7 7 0 0 0-7-7z" fill="#fff"/><circle cx="7" cy="7" r="2.6" fill="#0c2744"/></svg><p>The Redemption Center<br>4410 Harbor View Rd Ste 12<br>Cedar Point, Ca 90417</p></div>
  </div>
  <div class="f-rule"></div>
  <div class="copyright">Copyright©2020 Bounty Motivation Delivery Networks. All Rights Reserved.</div>
</footer>

</body>
</html>
```